Silver Heron Construction Services

Create a business card for my business consulting company
Danielle Vesk, Founder and CEO
4816 Alder Brook Way, Ste 100
Denver, CO. 80451
303.782.4190 cell
dvesk@silverheronconst.example
www.silverheronconst.example

Target Market(s)

Private Equity and Construction Companies

Industry/Entity Type

Business / Sales Consulting

Contact Information for Business Card

Tag Line that says "Where The Road To Success Is Always Under Construction"

Requirements
Must have
• Logo on both sides of the card.
Nice to have
• Add tagline to the same side of the card as my name and contact info

```html
<!DOCTYPE html>
<html lang="en">
<head>
<meta charset="utf-8">
<title>Silver Heron Construction Services — Business Card</title>
<link href="https://fonts.googleapis.com/css2?family=Montserrat:wght@400;500;600&family=Newsreader:ital,opsz,wght@0,6..72,400;1,6..72,400&display=swap" rel="stylesheet">
<style>
  :root {
    --backdrop: #ababab;
    --card-light: #ffffff;
    --card-dark: #282828;
    --ink: #1a1a1a;
    --ink-soft: #7a7a7a;
    --mark-dark: #1c1c1c;
    --url-dark: #8c8c8c;
    --serif: "Newsreader", Georgia, serif;
    --sans: "Montserrat", Arial, sans-serif;
  }
  * { margin: 0; padding: 0; box-sizing: border-box; }
  html, body { width: 1200px; height: 1000px; overflow: hidden; }
  body { background: var(--backdrop); position: relative; font-family: var(--sans); }

  .card { position: absolute; width: 613px; height: 352px; border-radius: 22px; }
  .card--front { left: 292px; top: 126px; background: var(--card-light); }
  .card--back { left: 294px; top: 531px; background: var(--card-dark); }

  .brand-small {
    position: absolute; right: 28px; top: 48px; width: 110px;
    text-align: center; font-family: var(--sans); font-weight: 600;
    font-size: 11px; line-height: 1.2; letter-spacing: 0.04em;
    color: var(--ink); text-transform: uppercase;
  }

  .tagline {
    position: absolute; left: 61px; top: 130px; width: 250px;
    font-family: var(--serif); font-size: 32px; line-height: 38.5px;
    color: var(--ink);
  }

  .contact { position: absolute; left: 346px; top: 124px; }
  .contact__name {
    font-family: var(--serif); font-style: italic; font-size: 22px;
    line-height: 1; color: var(--ink);
  }
  .contact__title { font-size: 12px; color: var(--ink); margin-top: 5px; }
  .contact__rule { width: 52px; height: 1px; background: var(--ink); margin-top: 8px; }
  .contact__block { font-size: 12.5px; line-height: 16px; color: var(--ink-soft); margin-top: 13px; letter-spacing: 0.01em; }
  .contact__block + .contact__block { margin-top: 15px; }
  .contact__label { color: var(--ink); }

  .brand-large {
    position: absolute; left: 0; right: 0; top: 145px; text-align: center;
    font-family: var(--sans); font-weight: 600; font-size: 27px;
    line-height: 1.2; letter-spacing: 0.03em; color: var(--mark-dark);
    text-transform: uppercase;
  }
  .back-url {
    position: absolute; left: 0; right: 0; top: 302px; text-align: center;
    font-size: 16px; color: var(--url-dark); letter-spacing: 0.01em;
  }
</style>
</head>
<body>
  <section class="card card--front">
    <div class="brand-small">Silver Heron Construction Services</div>
    <p class="tagline">“Where The Road To Success Is Always Under Construction”</p>
    <div class="contact">
      <p class="contact__name">Danielle Vesk</p>
      <p class="contact__title">Founder and CEO</p>
      <div class="contact__rule"></div>
      <p class="contact__block">4816 Alder Brook Way, Ste 100<br>Denver, CO. 80451</p>
      <p class="contact__block">303.782.4190 <span class="contact__label">cell</span><br>dvesk@silverheronconst.example<br>www.silverheronconst.example</p>
    </div>
  </section>

  <section class="card card--back">
    <div class="brand-large">Silver Heron<br>Construction Services</div>
    <p class="back-url">silverheronconst.example</p>
  </section>
</body>
</html>
```